PRVD Traditional Business Card Project

Please see attached....just a simple business card... on attachment- please use the exact font, style, etc as the attached "Pat Everard Wynne" card... however, replace with the "Owen Reginald Talbot" text and address below the card.

```html
<!DOCTYPE html>
<html lang="en">
<head>
<meta charset="utf-8">
<title>PRVD Business Card</title>
<link rel="stylesheet" href="https://fonts.googleapis.com/css2?family=Cinzel:wght@400;500&family=Montserrat:wght@300;400&display=swap">
<style>
  :root {
    --backdrop: #2b2b2d;
    --card: #ffffff;
    --ink: #111111;
    --rule: #444444;
  }
  * { box-sizing: border-box; margin: 0; padding: 0; }
  html, body { width: 1200px; height: 880px; overflow: hidden; }
  body { background: var(--backdrop); position: relative; font-family: "Montserrat", sans-serif; color: var(--ink); }

  .card {
    position: absolute;
    width: 665px;
    height: 380px;
    background: var(--card);
    border-radius: 22px;
  }
  .card--back { left: 200px; top: 40px; }
  .card--front { left: 335px; top: 460px; }

  .brand-mark {
    display: flex;
    align-items: center;
    gap: 10px;
    font-family: "Cinzel", serif;
    font-weight: 500;
    color: var(--ink);
  }
  .brand-mark__square { width: 14px; height: 14px; border: 2px solid var(--ink); }

  .card--back .brand-mark { position: absolute; left: 0; right: 0; top: 130px; justify-content: center; font-size: 64px; letter-spacing: 4px; }
  .card--back .website { position: absolute; left: 0; right: 0; bottom: 46px; text-align: center; font-size: 15px; letter-spacing: 2px; }

  .card--front .brand-mark { position: absolute; right: 42px; top: 34px; font-size: 38px; letter-spacing: 2px; }

  .firm { position: absolute; left: 42px; top: 88px; }
  .firm__name { font-family: "Cinzel", serif; font-size: 34px; font-weight: 500; line-height: 1; }
  .firm__type { font-size: 15px; font-weight: 300; letter-spacing: 7.5px; margin-top: 4px; text-transform: uppercase; }

  .rule { position: absolute; height: 1px; background: var(--rule); }
  .rule--long { left: 42px; right: 42px; top: 178px; }
  .rule--short { left: 42px; width: 250px; top: 292px; }

  .attorney { position: absolute; left: 42px; top: 226px; }
  .attorney__name { font-family: "Cinzel", serif; font-size: 25px; font-weight: 500; line-height: 1; }
  .attorney__title { font-size: 14px; letter-spacing: 3px; text-transform: uppercase; margin-top: 6px; }

  .address { position: absolute; left: 42px; top: 304px; font-size: 14px; line-height: 21px; }

  .contact { position: absolute; right: 42px; top: 194px; list-style: none; font-size: 14px; line-height: 22px; text-align: right; }
  .contact li { display: flex; justify-content: flex-end; align-items: center; gap: 6px; }
  .contact svg { width: 12px; height: 12px; fill: var(--ink); }
</style>
</head>
<body>
  <section class="card card--back">
    <div class="brand-mark"><span class="brand-mark__square"></span>PRVD</div>
    <p class="website">WWW.PRVDLAW.COM</p>
  </section>

  <section class="card card--front">
    <div class="brand-mark"><span class="brand-mark__square"></span>PRVD</div>

    <div class="firm">
      <p class="firm__name">Pacific Ridge</p>
      <p class="firm__type">Valley Defenders, PLC</p>
    </div>

    <div class="rule rule--long"></div>

    <ul class="contact">
      <li>(555) 214-3800
        <svg viewBox="0 0 24 24" aria-hidden="true"><path d="M6.6 10.8a15 15 0 0 0 6.6 6.6l2.2-2.2a1 1 0 0 1 1-.25 11.4 11.4 0 0 0 3.6.57 1 1 0 0 1 1 1V20a1 1 0 0 1-1 1A17 17 0 0 1 3 4a1 1 0 0 1 1-1h3.5a1 1 0 0 1 1 1c0 1.25.2 2.45.57 3.57a1 1 0 0 1-.25 1z"/></svg></li>
      <li>(555) 214-3801
        <svg viewBox="0 0 24 24" aria-hidden="true"><path d="M6 3h12v5H6zM4 9h16a2 2 0 0 1 2 2v6h-4v4H6v-4H2v-6a2 2 0 0 1 2-2zm4 7v3h8v-3z"/></svg></li>
      <li>talbot@prvdlaw.com
        <svg viewBox="0 0 24 24" aria-hidden="true"><path d="M2 5h20v14H2zm2 2v.5l8 5 8-5V7l-8 5z"/></svg></li>
    </ul>

    <div class="attorney">
      <p class="attorney__name">Owen Reginald Talbot</p>
      <p class="attorney__title">Attorney at Law</p>
    </div>

    <div class="rule rule--short"></div>

    <p class="address">2740 Cedar Lane, Suite B<br>Alder Springs, CA 91502<br>www.prvdlaw.com</p>
  </section>
</body>
</html>
```